Meridian Dash add on sales tool2017

This will be a flyer to leave with our clients we just did work for. We want to entice them to use our other services over the next 30 days with a discount, money off etc. we will write in the special and the expiration date. I want the client to read the description and see a picture of the service they may want done.

Target Market(s)

Repeat clients

Industry/Entity Type

Cleaning Service

Font styles to use
Serif
Sans Serif

Colors
ec1f27
000000
b1b1b1

Requirements
Must have
• Call to action! look high end market, clients show we do 1st class work.
• Don't Waite
Nice to have
• Classy, quality, I'm open to using other pictures that may look better
Should not have
• Look like a typical carpet cleaners special flyer
• Not to look cluttered

```html
<!DOCTYPE html>
<html lang="en">
<head>
<meta charset="utf-8">
<title>Meridian Dash – Add-On Services Flyer</title>
<link href="https://fonts.googleapis.com/css2?family=PT+Sans:wght@400;700&family=PT+Serif:wght@400;700&display=swap" rel="stylesheet">
<style>
  :root {
    --brand-red: #ec1f27;
    --ink: #000000;
    --silver: #b1b1b1;
    --paper: #f3f3f3;
    --body-text: #3a3a3a;
    --footer-dark: #141414;
    --white: #ffffff;
  }
  * { box-sizing: border-box; margin: 0; padding: 0; }
  html, body { width: 1003px; height: 1200px; overflow: hidden; }
  body { background: var(--paper); font-family: "PT Sans", sans-serif; position: relative; }

  .hero {
    position: absolute; left: 0; top: 0; width: 1003px; height: 515px;
    background:
      linear-gradient(180deg, rgba(10,10,10,0) 60%, rgba(0,0,0,0.15) 100%),
      radial-gradient(ellipse at 45% 85%, #8e1d22 0%, #6b2320 30%, rgba(107,35,32,0) 60%),
      linear-gradient(100deg, #d9d2c6 0%, #b8a68c 35%, #cfc6b6 60%, #7a5634 100%);
  }
  .header-band {
    position: absolute; left: 0; top: 0; width: 1003px; height: 170px;
    background: linear-gradient(180deg, rgba(12,12,12,0.97) 0%, rgba(20,20,20,0.9) 100%);
  }
  .header-band svg { position: absolute; left: 0; bottom: -20px; }
  .brand {
    position: absolute; left: 0; top: 24px; width: 1003px; text-align: center;
  }
  .brand-dot {
    display: block; width: 76px; height: 76px; margin: 0 auto 14px;
    border-radius: 50%; background: var(--brand-red);
  }
  .brand-name {
    font-family: "PT Sans", sans-serif; font-weight: 700; font-size: 28px;
    color: var(--brand-red); letter-spacing: 0.5px; text-transform: uppercase; line-height: 1;
  }
  .headline {
    position: absolute; left: 112px; top: 282px; width: 860px;
    font-family: "PT Serif", serif; font-weight: 700; font-size: 50px; line-height: 1.33;
    color: var(--white); text-transform: uppercase; letter-spacing: -0.5px;
    text-shadow: 0 2px 6px rgba(0,0,0,0.35);
  }

  .service { position: absolute; width: 450px; height: 170px; }
  .service-photo {
    position: absolute; left: 0; top: 0; width: 164px; height: 160px; border-radius: 50%;
    border: 4px solid #d6d6d6; box-shadow: 0 2px 6px rgba(0,0,0,0.25); overflow: hidden;
  }
  .service-photo .tag {
    position: absolute; bottom: 44px; font-family: "PT Serif", serif; font-size: 12px; color: var(--white);
  }
  .service-photo .tag.before { left: 30px; }
  .service-photo .tag.after { left: 100px; }
  .service-title {
    position: absolute; left: 125px; top: 8px; width: 275px; height: 32px;
    background: linear-gradient(90deg, rgba(236,31,39,0) 0%, rgba(236,31,39,0.75) 22%, var(--brand-red) 45%);
    border-top-right-radius: 8px;
    font-family: "PT Serif", serif; font-size: 16px; color: var(--white);
    line-height: 32px; padding-left: 50px; text-transform: uppercase; white-space: nowrap;
  }
  .service-copy {
    position: absolute; left: 177px; top: 55px; width: 270px;
    font-size: 15px; line-height: 1.18; color: var(--body-text); text-align: justify;
  }
  .stone .service-copy { width: 252px; }

  .carpet   { left: 30px;  top: 552px; }
  .drapery  { left: 30px;  top: 740px; }
  .stone    { left: 30px;  top: 929px; }
  .upholstery { left: 537px; top: 552px; }
  .tile     { left: 537px; top: 740px; }

  .offer {
    position: absolute; left: 555px; top: 935px; width: 401px; height: 137px;
    background: #dcdcdc; border-radius: 8px; overflow: hidden;
  }
  .offer-title {
    position: absolute; left: 0; top: 0; width: 305px; height: 30px;
    background: var(--brand-red); border-bottom-right-radius: 8px;
    font-family: "PT Serif", serif; font-size: 19px; color: var(--white);
    line-height: 30px; padding-left: 18px; text-transform: uppercase;
  }
  .offer-expires {
    position: absolute; left: 18px; bottom: 10px; font-size: 15px; color: #555;
  }

  .footer { position: absolute; left: 0; top: 1075px; width: 1003px; height: 125px; }
  .footer svg.bands { position: absolute; left: 0; top: 0; }
  .footer-address, .footer-call {
    position: absolute; top: 76px; font-family: "PT Serif", serif; color: var(--white);
    font-size: 20px; display: flex; align-items: center; gap: 8px; white-space: nowrap;
  }
  .footer-address { left: 34px; }
  .footer-call { right: 56px; }
  .footer-call .cta { margin-right: 14px; }
</style>
</head>
<body>

<section class="hero" role="img" aria-label="Photo of a bright living room with a white sofa, white grand piano and a red patterned rug on a wood floor"></section>

<header class="header-band">
  <svg width="1003" height="40" viewBox="0 0 1003 40" aria-hidden="true">
    <path d="M0 0 Q501 40 1003 0 L1003 0 L0 0 Z" fill="rgba(20,20,20,0.9)"/>
  </svg>
  <div class="brand">
    <span class="brand-dot" aria-hidden="true"></span>
    <div class="brand-name">Meridian Dash</div>
  </div>
</header>

<h1 class="headline">One stop for all your home cleaning needs</h1>

<article class="service carpet">
  <div class="service-title">Carpet Cleaning</div>
  <div class="service-photo" role="img" aria-label="Photo of a carpet being cleaned with water spray" style="background: radial-gradient(circle at 50% 45%, #f2f4f6 0%, #b9bfc4 35%, #5e5352 75%, #3c2c2a 100%);"></div>
  <p class="service-copy">Don't let dirty carpets spoil the look of your beautiful home! With 37 years of cleaning carpets experience you can expect your carpets to look like new in most cases.</p>
</article>

<article class="service drapery">
  <div class="service-title">Darapery Cleaning</div>
  <div class="service-photo" role="img" aria-label="Photo of a technician cleaning drapes at a window" style="background: linear-gradient(90deg, #8b6b57 0%, #c9b8a6 30%, #2b2b2b 55%, #d9dde0 80%, #a9a39a 100%);"></div>
  <p class="service-copy">Drapery's act like a filter atracting atmisphiric soil! Making them look dingy. We make it easy to Dry clean in home! Safe and efective beautiful drapery again.</p>
</article>

<article class="service stone">
  <div class="service-title">Natural Stone Cleaning</div>
  <div class="service-photo" role="img" aria-label="Photo of a polished marble floor in a bright room" style="background: linear-gradient(180deg, #d7d3c8 0%, #a7a39a 40%, #6e6c66 75%, #55524c 100%);"></div>
  <p class="service-copy">Cleaning &amp; Polishing. A dull stained Marble - Granite-Travertine and other Natural stone can be revitalized to look NEW again!</p>
</article>

<article class="service upholstery">
  <div class="service-title">Upholstery Cleaning</div>
  <div class="service-photo" role="img" aria-label="Before and after photo of a cleaned striped sofa cushion" style="background: linear-gradient(90deg, #4f5a52 0%, #8a9188 48%, #e8e8e8 50%, #b7b8ae 52%, #c9c5b6 100%);">
    <span class="tag before">before</span><span class="tag after">after</span>
  </div>
  <p class="service-copy">Every day use leaves your sofa's and chairs lookng dingy and can smell like dog. Our Dry cleaning, Shampoo or Rinse extraxtion will leave the fabric feel like clean sheet!</p>
</article>

<article class="service tile">
  <div class="service-title">Tile &amp; Grout Cleaning</div>
  <div class="service-photo" role="img" aria-label="Before and after photo of cleaned floor tile and grout" style="background: linear-gradient(135deg, #6a6661 0%, #8d8983 45%, #b9b6b0 55%, #a6a29c 100%);">
    <span class="tag before">before</span><span class="tag after">after</span>
  </div>
  <p class="service-copy">Tile &amp; Grout get neglected! Dirty grout can leave permanent staining. Let our professionals bring back the look of a new floor.</p>
</article>

<aside class="offer">
  <div class="offer-title">30 Day Special Offer!</div>
  <div class="offer-expires">Expires</div>
</aside>

<footer class="footer">
  <svg class="bands" width="1003" height="125" viewBox="0 0 1003 125" aria-hidden="true">
    <defs>
      <radialGradient id="footerGlow" cx="0.5" cy="0.6" r="0.6">
        <stop offset="0" stop-color="#4a4a4a"/>
        <stop offset="1" stop-color="#141414"/>
      </radialGradient>
    </defs>
    <path d="M0 0 Q501 58 1003 0 L1003 125 L0 125 Z" fill="#ec1f27"/>
    <path d="M0 12 Q501 66 1003 10 L1003 125 L0 125 Z" fill="url(#footerGlow)"/>
  </svg>
  <div class="footer-address">
    <svg width="12" height="18" viewBox="0 0 12 18" aria-hidden="true"><path d="M6 0a6 6 0 0 0-6 6c0 4.5 6 12 6 12s6-7.5 6-12a6 6 0 0 0-6-6zm0 8.5A2.5 2.5 0 1 1 6 3.5a2.5 2.5 0 0 1 0 5z" fill="#ffffff"/></svg>
    1480 W. Larkspur Ave. Suite C Las Vegas
  </div>
  <div class="footer-call">
    <span class="cta">CALL NOW TO BOOK</span>
    <svg width="17" height="17" viewBox="0 0 24 24" aria-hidden="true"><path d="M6.6 10.8a15.1 15.1 0 0 0 6.6 6.6l2.2-2.2c.3-.3.7-.4 1-.2 1.1.4 2.3.6 3.6.6.6 0 1 .4 1 1V20c0 .6-.4 1-1 1A17 17 0 0 1 3 4c0-.6.4-1 1-1h3.5c.6 0 1 .4 1 1 0 1.3.2 2.5.6 3.6.1.3 0 .7-.2 1z" fill="#ffffff"/></svg>
    <span>702 555-0147</span>
  </div>
</footer>

</body>
</html>
```